Harvest Cobbler Bash

I am a Realtor and will be Mailing this Postcard to my best Clients Inviting them to Select the Pie they want for Thanksgiving and I will open my office for them to pick up. here's my thought on text:

THANK YOU HARVEST COBBLER BASH!
Tues Nov 25th 3 to 8PM

In Giving Thanks for Your Support and Referrals I want to Personally Invite You to My 1st Annual "Harvest Cobbler Bash". You have a choice of:
*Apple
*Pumpkin
*Pecan

Please let me know Your Choice by Mon Nov 17th. Please Feel Free to email me or Call Me with Your Pie Choice!

There will be Food and Drink Including My Award Winning Chili.

718 Larchmont Road
Gorham Me 04915
dana@danawhitmer.com
207.555.0148

Please Give it a Thanksgiving Look....I did not include a photo of a pie but open to it. PLEASE make the Paragraph "In Giving Thanks with the 3 Pie choices the Focal Point that Draws Your eyes to it.

```html
<!DOCTYPE html>
<html lang="en">
<head>
<meta charset="utf-8">
<title>Harvest Cobbler Bash – Thank You Card</title>
<link href="https://fonts.googleapis.com/css2?family=Cinzel:wght@500;700&family=Great+Vibes&family=Cormorant+Garamond:ital,wght@0,500;0,600;1,500&display=swap" rel="stylesheet">
<style>
  :root {
    --backdrop: #2a2a2a;
    --maroon: #5e0f0f;
    --gold: #c9962e;
    --gold-script: #f2b53c;
    --cream: #fbf3e6;
    --cream-soft: #ecdcc4;
    --crust-light: #f2d79a;
    --crust-mid: #e0b461;
    --crust-dark: #b9823a;
    --leaf-red: #c2411a;
    --leaf-orange: #e9872a;
    --leaf-yellow: #d9a93a;
  }
  * { margin: 0; padding: 0; box-sizing: border-box; }
  html, body {
    width: 1200px;
    height: 907px;
    overflow: hidden;
    background: var(--backdrop);
  }
  .postcard {
    position: absolute;
    left: 80px;
    top: 48px;
    width: 1040px;
    height: 807px;
    background: var(--maroon);
    overflow: hidden;
  }
  .postcard__rule {
    position: absolute;
    top: 0;
    width: 6px;
    height: 100%;
    background: var(--gold);
  }
  .postcard__rule--left { left: 42px; }
  .postcard__rule--right { left: 530px; }
  .postcard__photo {
    position: absolute;
    left: 60px;
    top: 0;
    width: 460px;
    height: 100%;
    background:
      radial-gradient(ellipse 70% 45% at 55% 40%, var(--crust-dark) 0%, var(--crust-mid) 35%, transparent 70%),
      radial-gradient(ellipse 95% 70% at 60% 60%, var(--crust-light) 0%, var(--crust-mid) 60%, transparent 85%),
      linear-gradient(180deg, #d9e2ec 0%, #c9d1da 18%, #e8c98a 40%, #e6bf72 75%, #d8d3c8 92%, #4a3326 100%);
  }
  .postcard__foliage {
    position: absolute;
    right: 0;
    top: 0;
    width: 340px;
    height: 245px;
    background:
      radial-gradient(ellipse 40% 45% at 30% 30%, var(--leaf-red) 0%, transparent 70%),
      radial-gradient(ellipse 40% 50% at 70% 35%, var(--leaf-orange) 0%, transparent 70%),
      radial-gradient(ellipse 35% 40% at 45% 70%, var(--leaf-yellow) 0%, transparent 70%);
    opacity: 0.9;
  }
  .message {
    position: absolute;
    right: 36px;
    top: 252px;
    width: 440px;
    display: flex;
    flex-direction: column;
    align-items: flex-end;
    text-align: right;
  }
  .message__headline {
    font-family: "Cinzel", serif;
    font-weight: 500;
    font-size: 30px;
    line-height: 36px;
    letter-spacing: 1px;
    color: var(--cream);
  }
  .message__script {
    margin-top: 6px;
    font-family: "Great Vibes", cursive;
    font-size: 80px;
    line-height: 86px;
    color: var(--gold-script);
    white-space: nowrap;
  }
  .message__date {
    margin-top: 4px;
    font-family: "Cinzel", serif;
    font-weight: 700;
    font-size: 18px;
    line-height: 24px;
    letter-spacing: 1px;
    color: var(--gold-script);
  }
  .message__invite {
    margin-top: 10px;
    font-family: "Cormorant Garamond", serif;
    font-weight: 600;
    font-size: 18px;
    line-height: 22px;
    color: var(--cream);
  }
  .message__choices {
    margin-top: 8px;
    display: flex;
    gap: 18px;
    list-style: none;
    font-family: "Cinzel", serif;
    font-weight: 700;
    font-size: 22px;
    line-height: 28px;
    color: var(--gold-script);
  }
  .message__rsvp {
    margin-top: 8px;
    font-family: "Cormorant Garamond", serif;
    font-style: italic;
    font-weight: 500;
    font-size: 14px;
    line-height: 18px;
    color: var(--cream-soft);
  }
  .agent {
    position: absolute;
    right: 36px;
    top: 664px;
    text-align: right;
  }
  .agent__brand {
    font-family: "Cinzel", serif;
    font-weight: 500;
    font-size: 26px;
    line-height: 30px;
    letter-spacing: 1px;
    color: #ffffff;
  }
  .agent__contact {
    margin-top: 8px;
    font-family: "Cormorant Garamond", serif;
    font-style: normal;
    font-weight: 600;
    font-size: 15px;
    line-height: 19px;
    color: var(--cream-soft);
  }
</style>
</head>
<body>
  <main class="postcard">
    <div class="postcard__rule postcard__rule--left"></div>
    <div class="postcard__photo" role="img" aria-label="Photograph of a golden rustic fruit galette with almond slices on a white plate"></div>
    <div class="postcard__rule postcard__rule--right"></div>
    <div class="postcard__foliage" role="img" aria-label="Illustration of red, orange and yellow autumn maple leaves"></div>

    <section class="message">
      <h1 class="message__headline">HARVEST<br>COBBLER BASH!</h1>
      <p class="message__script">Thank You</p>
      <p class="message__date">Tues Nov 25th · 3 to 8PM</p>
      <p class="message__invite">In Giving Thanks for Your Support and Referrals I want to Personally Invite You to My 1st Annual “Harvest Cobbler Bash”. You have a choice of:</p>
      <ul class="message__choices">
        <li>Apple</li>
        <li>Pumpkin</li>
        <li>Pecan</li>
      </ul>
      <p class="message__rsvp">Please let me know Your Choice by Mon Nov 17th by email or call.<br>There will be Food and Drink Including My Award Winning Chili.</p>
    </section>

    <footer class="agent">
      <p class="agent__brand">Harbor Point<br>Realty Group</p>
      <address class="agent__contact">718 Larchmont Road, Gorham Me 04915<br>dana@danawhitmer.com<br>207.555.0148</address>
    </footer>
  </main>
</body>
</html>
```